Redesign Business Cards, Attached

Please read instructions carefully. If you have any questions send a message before submitting your ONE design. Please redesign attached business cards. Double sided. Use same content and descriptions. Use black, silver, crimson red and gold colors. My only issue with the attached design is the background colors. I like the layout as-is. I can provide the individual pictures on the back side later. Do not submit more than one design. One submission shall include both front and back. Do not submit front and back separately. A second project will be launched to create a matching post card after completion of this.
Industry/Entity Type
see description and attachments.
Contact Information for Business Card
Requirements
Must have
- see description and attachments.
Nice to have
Should not have

```html
<!DOCTYPE html>
<html lang="en">
<head>
<meta charset="utf-8">
<title>Helmwise Boat Training – Business Card</title>
<link href="https://fonts.googleapis.com/css2?family=Montserrat:wght@600;700&family=Work+Sans:wght@400;500&display=swap" rel="stylesheet">
<style>
  :root {
    --backdrop: #8c8c8c;
    --card: #ffffff;
    --ink: #1d1d1d;
    --gold: #c9a227;
    --crimson: #d8202a;
    --navy: #1f3f8f;
    --sea-deep: #23344a;
    --sea-mid: #5e7a96;
    --sea-light: #c9d6e2;
    --band: rgba(10, 12, 16, 0.88);
  }
  * { margin: 0; padding: 0; box-sizing: border-box; }
  html, body { width: 1200px; height: 1200px; overflow: hidden; }
  body {
    background: var(--backdrop);
    position: relative;
    font-family: "Work Sans", Arial, sans-serif;
    color: var(--ink);
  }
  .card {
    position: absolute;
    left: 281px;
    width: 642px;
    height: 366px;
    border-radius: 16px;
    overflow: hidden;
  }
  .card--front { top: 195px; background: var(--card); }
  .card--back { top: 639px; }

  /* front */
  .brand {
    position: absolute;
    left: 440px; top: 50px;
    width: 180px; height: 130px;
    display: flex; flex-direction: column; align-items: center; justify-content: center;
    gap: 10px;
  }
  .brand__dot {
    width: 26px; height: 26px; border-radius: 50%;
    background: var(--gold);
  }
  .brand__name {
    font-family: "Montserrat", Arial, sans-serif;
    font-weight: 700;
    font-size: 16px;
    line-height: 1.25;
    text-align: center;
    color: var(--ink);
    text-transform: uppercase;
    letter-spacing: 0.5px;
  }
  .holder {
    position: absolute;
    left: 29px; top: 168px;
  }
  .holder__name {
    font-family: "Montserrat", Arial, sans-serif;
    font-weight: 700;
    font-size: 25px;
    color: var(--gold);
    line-height: 1;
    margin-bottom: 8px;
  }
  .holder__title {
    font-size: 18px;
    line-height: 22px;
    color: var(--ink);
  }
  .divider {
    position: absolute;
    left: 29px; top: 254px;
    width: 583px; height: 2px;
    background: var(--crimson);
  }
  .contacts {
    position: absolute;
    left: 29px; top: 271px;
    list-style: none;
  }
  .contacts__item {
    display: flex; align-items: center;
    height: 23px;
    font-size: 15px;
  }
  .contacts__item svg { width: 14px; height: 14px; margin-right: 12px; flex: none; }
  .contacts__item--phone { font-family: "Montserrat", Arial, sans-serif; font-weight: 600; font-size: 18px; }
  .badges {
    position: absolute;
    left: 478px; top: 276px;
    display: flex; gap: 12px; align-items: center;
  }
  .badge {
    width: 62px; height: 62px;
    border-radius: 50%;
  }
  .badge--member { background: var(--crimson); }
  .badge--instructor { background: var(--navy); }

  /* back */
  .sea-photo {
    position: absolute; inset: 0;
    background:
      radial-gradient(ellipse 30% 45% at 75% 50%, rgba(255,255,255,0.75), rgba(255,255,255,0) 70%),
      linear-gradient(160deg, var(--sea-mid) 0%, var(--sea-light) 45%, var(--sea-mid) 70%, var(--sea-deep) 100%);
  }
  .services {
    position: absolute;
    left: 0; top: 53px;
    list-style: none;
  }
  .services__item {
    display: flex; align-items: center;
    width: max-content;
    min-width: 370px; height: 27px;
    margin-bottom: 6.2px;
    padding-left: 22px;
    padding-right: 30px;
    background: linear-gradient(90deg, var(--band) 0%, var(--band) 60%, rgba(10,12,16,0) 100%);
    color: #ffffff;
    font-size: 16px;
    white-space: nowrap;
  }
  .services__item::before {
    content: "";
    width: 7px; height: 7px; border-radius: 50%;
    background: var(--gold);
    margin-right: 12px;
    flex: none;
  }
</style>
</head>
<body>

<section class="card card--front">
  <div class="brand">
    <span class="brand__dot"></span>
    <span class="brand__name">Helmwise<br>Boat Training</span>
  </div>

  <div class="holder">
    <h1 class="holder__name">DALTON R. WHITMORE</h1>
    <p class="holder__title">USCG Licensed Captain</p>
    <p class="holder__title">Certified Instructor</p>
  </div>

  <div class="divider"></div>

  <ul class="contacts">
    <li class="contacts__item contacts__item--phone">
      <svg viewBox="0 0 24 24"><path fill="#c9a227" d="M6.6 10.8a15 15 0 0 0 6.6 6.6l2.2-2.2a1 1 0 0 1 1-.25 11.4 11.4 0 0 0 3.6.57 1 1 0 0 1 1 1V20a1 1 0 0 1-1 1A17 17 0 0 1 3 4a1 1 0 0 1 1-1h3.5a1 1 0 0 1 1 1c0 1.250.2 2.450.57 3.57a1 1 0 0 1-.25 1z"/></svg>
      Text (555) 014-2287
    </li>
    <li class="contacts__item">
      <svg viewBox="0 0 24 24"><rect x="2" y="5" width="20" height="14" fill="#c9a227"/><path d="M2 5l10 8 10-8" fill="none" stroke="#fff" stroke-width="1.8"/></svg>
      service@helmwiseboating.com
    </li>
    <li class="contacts__item">
      <svg viewBox="0 0 24 24"><circle cx="12" cy="12" r="10" fill="#c9a227"/><path d="M2 12h20M12 2c3 3 3 17 0 20M12 2c-3 3-3 17 0 20" fill="none" stroke="#fff" stroke-width="1.4"/></svg>
      www.helmwiseboating.com
    </li>
  </ul>

  <div class="badges">
    <div class="badge badge--member" role="img" aria-label="Partner membership badge"></div>
    <div class="badge badge--instructor" role="img" aria-label="Instructor certification badge"></div>
  </div>
</section>

<section class="card card--back">
  <div class="sea-photo" role="img" aria-label="Photo of a white center-console power boat cruising across open water, leaving a foamy wake"></div>
  <ul class="services">
    <li class="services__item">Hands-On Boat Training</li>
    <li class="services__item">Introduction to Power Boating</li>
    <li class="services__item">Precision Docking &amp; Boat Handling</li>
    <li class="services__item">Open Water Boat Handling</li>
    <li class="services__item">Inland Anchoring</li>
    <li class="services__item">Open Water Advanced Maneuvers</li>
    <li class="services__item">Coastal Navigation</li>
    <li class="services__item">Captaining / Piloting Service for Your Outings</li>
  </ul>
</section>

</body>
</html>
```